Business Card Design

We have our logo and everything in place. Looking to have a layout for our new business cards designed. These will be printed with a matte finish, possibly rounded corners, and looking to incorporate some cool spot UV layers into the design.

Ive uploaded the existing card front and back as well as our logo.

Card Size Will Be 3.5" x 2"

```html
<!DOCTYPE html>
<html lang="en">
<head>
<meta charset="utf-8">
<title>Keystone Deck and Rail – Business Cards</title>
<link href="https://fonts.googleapis.com/css2?family=Arimo:wght@400;700&display=swap" rel="stylesheet">
<style>
  :root {
    --page: #ece9e4;
    --card-black: #0d0d0d;
    --card-black-hi: #262626;
    --panel-white: #ececec;
    --accent-blue: #2a8fd8;
    --ink: #1e1e1e;
    --logo-white: #f4f4f4;
    --rule-grey: #8a8a8a;
  }
  * { box-sizing: border-box; margin: 0; padding: 0; }
  html, body { width: 1200px; height: 950px; overflow: hidden; }
  body {
    background: var(--page);
    font-family: "Arimo", Arial, sans-serif;
    position: relative;
  }
  .card {
    position: absolute;
    left: 240px;
    width: 720px;
    height: 411px;
    border-radius: 26px;
    overflow: hidden;
    background: linear-gradient(150deg, var(--card-black-hi) 0%, var(--card-black) 45%);
    box-shadow: 0 14px 30px rgba(0,0,0,.28);
  }
  .card--front { top: 36px; }
  .card--back  { top: 500px; }

  .brand {
    position: absolute;
    color: var(--logo-white);
    font-family: "Arimo", Arial, sans-serif;
    font-weight: 400;
    text-align: center;
  }
  .brand__name { font-size: 46px; letter-spacing: 1px; line-height: 1; }
  .brand__sub {
    display: block;
    margin-top: 8px;
    padding-top: 6px;
    border-top: 1px solid var(--rule-grey);
    font-size: 11px;
    letter-spacing: 3px;
  }
  .card--front .brand { left: 190px; top: 140px; width: 340px; }
  .front-url {
    position: absolute;
    left: 0; right: 0; top: 260px;
    text-align: center;
    color: var(--logo-white);
    font-size: 17px;
    letter-spacing: 3.5px;
  }

  .back-art { position: absolute; inset: 0; }
  .card--back .brand { left: 40px; top: 130px; width: 260px; }
  .card--back .brand__name { font-size: 40px; }

  .contact {
    position: absolute;
    left: 440px;
    top: 175px;
    color: var(--ink);
  }
  .contact__name { color: var(--accent-blue); font-size: 24px; }
  .contact__role { font-size: 16px; margin: 4px 0 22px 20px; }
  .contact__line { display: flex; align-items: center; gap: 10px; font-size: 15.5px; margin-bottom: 8px; }
  .contact__icon { width: 16px; height: 16px; flex: none; }
</style>
</head>
<body>

<section class="card card--front" aria-label="Card front">
  <div class="brand">
    <div class="brand__name">Keystone</div>
    <span class="brand__sub">DECK AND RAIL</span>
  </div>
  <p class="front-url">www.keystonedeckandrail.com</p>
</section>

<section class="card card--back" aria-label="Card back">
  <svg class="back-art" viewBox="0 0 720 411" aria-hidden="true">
    <polyline points="268,411 328,168 432,80 720,80" fill="none" stroke="var(--accent-blue)" stroke-width="5"/>
    <polyline points="276,411 336,172 438,90 720,90" fill="none" stroke="var(--panel-white)" stroke-width="4"/>
    <polygon points="286,411 344,176 444,98 720,98 720,411" fill="var(--panel-white)"/>
  </svg>

  <div class="brand">
    <div class="brand__name">Keystone</div>
    <span class="brand__sub">DECK AND RAIL</span>
  </div>

  <div class="contact">
    <div class="contact__name">Martin Ellery</div>
    <div class="contact__role">President</div>
    <div class="contact__line">
      <svg class="contact__icon" viewBox="0 0 16 16"><path d="M3 1.5h3l1.2 3.3-1.8 1.2a8 8 0 0 0 4.6 4.6l1.2-1.8 3.3 1.2v3c0 .6-.5 1-1 1A12.5 12.5 0 0 1 2 2.5c0-.5.4-1 1-1z" fill="var(--accent-blue)"/></svg>
      <span>555.010.2944</span>
    </div>
    <div class="contact__line">
      <svg class="contact__icon" viewBox="0 0 16 16"><rect x="1" y="3" width="14" height="10" rx="1.5" fill="var(--accent-blue)"/><path d="M1.5 4l6.5 5 6.5-5" fill="none" stroke="var(--panel-white)" stroke-width="1.3"/></svg>
      <span>keystonedeckandrail@mail.com</span>
    </div>
    <div class="contact__line">
      <svg class="contact__icon" viewBox="0 0 16 16"><circle cx="8" cy="8" r="7" fill="var(--accent-blue)"/><path d="M1.5 8h13M8 1.2c2.2 2 2.2 11.6 0 13.6M8 1.2c-2.2 2-2.2 11.6 0 13.6" fill="none" stroke="var(--panel-white)" stroke-width="1"/></svg>
      <span>www.keystonedeckandrail.com</span>
    </div>
  </div>
</section>

</body>
</html>
```